Geschäftspapiere für moderne Handwerksfirma
Zielgruppe
Wir sind eine moderne Handwerksfirma im Bereich Elektrotechnik und erneuerbare Energie. Unsere Zielgruppe sind Privatpersonen, Kommunen, Firmen, Landwirtschaften
Aufgabenstellung
Unser Design soll unser Logo, sowie unsere Hauptfarben anthrazit und rot aufweisen.

```html
<!DOCTYPE html>
<html lang="de">
<head>
<meta charset="utf-8">
<title>Brandt Energie – Geschäftspapiere</title>
<link href="https://fonts.googleapis.com/css2?family=Open+Sans:wght@400;600;700&display=swap" rel="stylesheet">
<style>
  :root{
    --red:#d0101e;
    --anthracite:#3e4a4c;
    --paper:#ffffff;
    --backdrop:#dcdcdc;
    --text:#444;
  }
  *{box-sizing:border-box;margin:0;padding:0}
  html,body{width:1200px;height:823px;overflow:hidden;background:var(--backdrop);font-family:"Open Sans",sans-serif;color:var(--text)}
  .sheet{position:absolute;background:var(--paper);box-shadow:3px 4px 8px rgba(0,0,0,.18);overflow:hidden}
  .band{position:absolute;left:0;display:block}
  .band path{}
  .fill-red{fill:var(--red)}
  .fill-dark{fill:var(--anthracite)}

  .logo{position:absolute;display:flex;align-items:center;gap:.35em}
  .logo-dot{display:block;border-radius:50%;background:var(--red);flex:none}
  .logo-name{font-weight:600;color:var(--red);line-height:1;letter-spacing:.02em}

  .icon{width:7px;height:7px;display:inline-block;vertical-align:-1px;margin-right:5px;fill:none;stroke:var(--red);stroke-width:1.4}
  .icon.solid{fill:var(--red);stroke:none}

  /* letterhead */
  .letterhead{left:36px;top:30px;width:536px;height:758px}
  .letterhead .logo{left:62px;top:23px}
  .letterhead .logo-dot{width:42px;height:42px}
  .letterhead .logo-name{font-size:24px}
  .sender-line{position:absolute;left:63px;top:116px;font-size:5.4px;font-weight:600;color:#555}
  .sender-line .sep{color:var(--red);margin:0 3px}
  .head-address{position:absolute;left:407px;top:29px;font-size:7px;line-height:10px;font-weight:700;color:var(--red)}
  .head-contact{position:absolute;left:407px;top:71px;font-size:7px;line-height:10px;color:#555}
  .fold-mark{position:absolute;left:0;height:1px;background:#bbb}
  .watermark{position:absolute;left:286px;top:370px;width:220px;height:220px;border-radius:50%;background:#f1f1f1}
  .footer-col{position:absolute;top:707px;font-size:6.2px;line-height:10px;color:#555}
  .footer-col .title{font-weight:700;color:var(--red)}
  .footer-col.company{font-weight:700;color:var(--red)}

  /* envelope front */
  .envelope-front{left:602px;top:30px;width:562px;height:281px}
  .envelope-front .logo{left:49px;top:40px}
  .envelope-front .logo-dot{width:34px;height:34px}
  .envelope-front .logo-name{font-size:19px}
  .envelope-sender{position:absolute;left:218px;top:53px;font-size:8px;line-height:10px;color:#222}
  .address-window{position:absolute;left:51px;top:128px;width:229px;height:115px;border:1px solid #9aa;border-radius:8px}

  /* envelope back */
  .envelope-back{left:602px;top:326px;width:561px;height:280px;box-shadow:3px 4px 8px rgba(0,0,0,.18)}
  .flap{position:absolute;left:0;top:0}
  .envelope-back .logo{left:212px;top:14px}
  .envelope-back .logo-dot{width:32px;height:32px}
  .envelope-back .logo-name{font-size:18px}

  /* business cards */
  .card-front{left:604px;top:646px;width:217px;height:141px}
  .card-front .logo{left:14px;top:12px}
  .card-front .logo-dot{width:28px;height:28px}
  .card-front .logo-name{font-size:15px}
  .card-person{position:absolute;left:13px;top:65px;font-size:8px;color:#444}
  .card-person strong{color:var(--red);font-weight:700}
  .card-address{position:absolute;left:13px;top:95px;font-size:6px;line-height:9.5px;font-weight:700;color:#333}
  .card-contact{position:absolute;left:104px;top:95px;font-size:6px;line-height:9.5px;color:#555}
  .card-contact .icon{width:6px;height:6px;margin-right:4px}

  .card-back{left:848px;top:648px;width:217px;height:140px;background:var(--anthracite)}
  .card-back .logo{left:38px;top:42px}
  .card-back .logo-dot{width:34px;height:34px}
  .card-back .logo-name{font-size:19px}
  .card-url{position:absolute;left:0;right:0;top:111px;text-align:center;font-size:9.5px;font-weight:700;color:#fff}
</style>
</head>
<body>

<svg width="0" height="0" style="position:absolute" aria-hidden="true">
  <symbol id="i-phone" viewBox="0 0 10 10"><path class="solid" d="M2 0.5 L3.8 2.6 L2.9 3.6 Q4 6 6.4 7.1 L7.4 6.2 L9.5 8 L8.3 9.5 Q2 9 0.5 1.7Z" fill="currentColor" stroke="none"/></symbol>
  <symbol id="i-fax" viewBox="0 0 10 10"><rect x="1" y="4" width="8" height="5" rx="1"/><rect x="3" y="1" width="4" height="3"/></symbol>
  <symbol id="i-mail" viewBox="0 0 10 10"><rect x="0.5" y="2" width="9" height="6.5" fill="currentColor" stroke="none"/><path d="M0.8 2.3 L5 5.8 L9.2 2.3" stroke="#fff" stroke-width="1"/></symbol>
  <symbol id="i-web" viewBox="0 0 10 10"><circle cx="5" cy="5" r="4.2"/><path d="M0.8 5 H9.2 M5 0.8 Q2 5 5 9.2 M5 0.8 Q8 5 5 9.2"/></symbol>
</svg>

<!-- Letterhead -->
<section class="sheet letterhead" aria-label="Briefbogen">
  <svg class="band" style="top:0" width="536" height="14" viewBox="0 0 536 14">
    <path class="fill-red" d="M0 0 H381 Q384 3 386 6.5 H0Z"/>
    <path class="fill-dark" d="M389 0 H536 V14 H399 Q393 13 389 0Z"/>
  </svg>

  <div class="logo"><span class="logo-dot"></span><span class="logo-name">BRANDT<br>ENERGIE</span></div>

  <div class="head-address">Brandt Energie GmbH<br>Am Lindenweg 12<br>87400 Talheim</div>
  <div class="head-contact">
    <div><svg class="icon" style="color:var(--red)"><use href="#i-phone"/></svg>08370/45120-0</div>
    <div><svg class="icon"><use href="#i-fax"/></svg>08370/45120-99</div>
    <div><svg class="icon" style="color:var(--red)"><use href="#i-mail"/></svg>info@brandt-energie.de</div>
    <div><svg class="icon"><use href="#i-web"/></svg>www.brandt-energie.de</div>
  </div>

  <div class="sender-line">Brandt Energie GmbH<span class="sep">|</span>Am Lindenweg 12<span class="sep">|</span>87400 Talheim</div>

  <span class="fold-mark" style="top:225px;width:18px"></span>
  <span class="fold-mark" style="top:382px;width:26px"></span>
  <span class="fold-mark" style="top:495px;width:18px"></span>

  <div class="watermark" role="img" aria-label="Dezente Hintergrundfläche"></div>

  <div class="footer-col company" style="left:63px">Brandt Energie GmbH<br>Am Lindenweg 12<br>87400 Talheim</div>
  <div class="footer-col" style="left:155px"><span class="title">Geschäftsführer:</span><br>Jonas Brandt</div>
  <div class="footer-col" style="left:218px">
    <div><svg class="icon" style="color:var(--red)"><use href="#i-phone"/></svg>08370/45120-0</div>
    <div><svg class="icon"><use href="#i-fax"/></svg>08370/45120-99</div>
    <div><svg class="icon" style="color:var(--red)"><use href="#i-mail"/></svg>info@brandt-energie.de</div>
    <div><svg class="icon"><use href="#i-web"/></svg>www.brandt-energie.de</div>
  </div>
  <div class="footer-col" style="left:304px"><span class="title">Amtsgericht:</span><br>Talheim HRB 20431<br>UST-ID: DE-314208867<br>Steuernummer: 131/442/10583</div>
  <div class="footer-col" style="left:407px"><span class="title">Bankverbindung:</span><br>Volksbank Talheim-Allgäu<br>IBAN: DE12 7205 1840 0003 4471 29<br>BIC: GENODEF1TAL</div>

  <svg class="band" style="bottom:0" width="536" height="14" viewBox="0 0 536 14">
    <path class="fill-dark" d="M0 0 H144 Q148 1 152 14 H0Z"/>
    <path class="fill-red" d="M152 7.5 H536 V14 H155 Q154 10 152 7.5Z"/>
  </svg>
</section>

<!-- Envelope front -->
<section class="sheet envelope-front" aria-label="Briefumschlag Vorderseite">
  <svg class="band" style="top:0" width="562" height="14" viewBox="0 0 562 14">
    <path class="fill-red" d="M0 0 H400 Q403 3 405 6.5 H0Z"/>
    <path class="fill-dark" d="M408 0 H562 V14 H418 Q412 13 408 0Z"/>
  </svg>
  <div class="logo"><span class="logo-dot"></span><span class="logo-name">BRANDT<br>ENERGIE</span></div>
  <div class="envelope-sender">Brandt Energie GmbH<br>Am Lindenweg 12<br>87400 Talheim</div>
  <div class="address-window"></div>
  <svg class="band" style="bottom:0" width="562" height="14" viewBox="0 0 562 14">
    <path class="fill-dark" d="M0 0 H148 Q152 1 156 14 H0Z"/>
    <path class="fill-red" d="M156 7.5 H562 V14 H159 Q158 10 156 7.5Z"/>
  </svg>
</section>

<!-- Envelope back -->
<section class="sheet envelope-back" aria-label="Briefumschlag Rückseite">
  <svg class="flap" width="561" height="64" viewBox="0 0 561 64">
    <path class="fill-dark" d="M0 0 H561 L541 55 Q537 63 528 63 H33 Q25 63 21 55Z"/>
  </svg>
  <div class="logo"><span class="logo-dot"></span><span class="logo-name">BRANDT<br>ENERGIE</span></div>
</section>

<!-- Business card front -->
<section class="sheet card-front" aria-label="Visitenkarte Vorderseite">
  <div class="logo"><span class="logo-dot"></span><span class="logo-name">BRANDT<br>ENERGIE</span></div>
  <div class="card-person">Jonas Brandt - <strong>Geschäftsführer</strong></div>
  <div class="card-address">Brandt Energie GmbH<br>Am Lindenweg 12<br>87400 Talheim</div>
  <div class="card-contact">
    <div><svg class="icon" style="color:var(--red)"><use href="#i-phone"/></svg>08370/45120-0</div>
    <div><svg class="icon"><use href="#i-fax"/></svg>08370/45120-99</div>
    <div><svg class="icon" style="color:var(--red)"><use href="#i-mail"/></svg>jonas.brandt@brandt-energie.de</div>
    <div><svg class="icon"><use href="#i-web"/></svg>www.brandt-energie.de</div>
  </div>
  <svg class="band" style="bottom:0" width="217" height="12" viewBox="0 0 217 12">
    <path class="fill-dark" d="M0 0 H78 Q81 1 83 12 H0Z"/>
    <path class="fill-red" d="M83 6.5 H217 V12 H85 Q84 9 83 6.5Z"/>
  </svg>
</section>

<!-- Business card back -->
<section class="sheet card-back" aria-label="Visitenkarte Rückseite">
  <div class="logo"><span class="logo-dot"></span><span class="logo-name">BRANDT<br>ENERGIE</span></div>
  <div class="card-url">www.brandt-energie.de</div>
</section>

</body>
</html>
```